website design for child care center
Maplebrook Academy
website design for child care center - Childcare
Creative Brief
Childcare
maplebrookacademytx.com
Maplebrook Academy is a child care center location- 3817 Route 221 N. Harlowville, NJ 08719 Phone number- 555-318-7042 Fax number- 555-318-7049 Email: main@maplebrookacademytx.com Hours of operation: 6:30 am to 6:30 pm Maplebrook Academy is an elite child care center housed in a state of the art facility. We are an owner operated facility that provides time honored traditional services. Slogan: Where Every Child Gets A Turn To Learn Owners: Rebecca Holt, Dana Pruitt, Karen Whitfield (we will be adding bio's about each owner later) Will service children ages 6 weeks to 6 years Curriculum- The Bright Pathways Program
likes: professional, clean lines, colorful kaleidoscopes rainbows whimsical dislikes: cheesy, messy, cluttered looking no animals or tacky looking clipart of children
blue
magenta
below header
http://www.totharbor.com/
http://www.sunpetalecc.com/
http://www.maplebrookacademykids.com/
Professional and playful

```html
<!DOCTYPE html>
<html lang="en">
<head>
<meta charset="utf-8">
<title>Maplebrook Academy</title>
<link href="https://fonts.googleapis.com/css2?family=Oswald:wght@400;500&family=Lato:wght@400;700&display=swap" rel="stylesheet">
<style>
:root{
  --sky:#4f9ad6;
  --sky-light:#9fd0f0;
  --grass:#a9cf3c;
  --grass-dark:#6ea51f;
  --nav-green:#8cc63f;
  --magenta:#e0197d;
  --pink:#e44a9c;
  --blue:#1b9ad6;
  --band-blue:#2a97d6;
  --lime:#8cc63f;
  --ink:#555;
  --ink-dark:#444;
  --gold:#f6c21c;
  --wood-light:#e39a48;
  --wood-dark:#c47a30;
  --bark:#3d2a14;
  --white:#fff;
}
*{margin:0;padding:0;box-sizing:border-box}
html,body{width:768px;height:1200px;overflow:hidden}
body{position:relative;font-family:"Lato",sans-serif;color:var(--ink);background:var(--grass)}
.abs{position:absolute}
.scenery{position:absolute;left:0;top:0;width:768px;height:1200px;
  background:linear-gradient(180deg,var(--sky) 0,var(--sky-light) 230px,#d6ecf5 260px,var(--grass) 300px,#c3dc62 440px,#c8dd7a 900px,#b7d56a 1100px,var(--grass-dark) 1200px)}
.topbar{font-family:"Oswald",sans-serif;font-size:9.5px;color:var(--gold)}
.topbar .row{display:flex;align-items:center;gap:5px;height:16px}
.topbar svg{width:10px;height:10px}
.topbar.right{text-align:right;right:104px;top:7px;line-height:19px}
.topbar.right .lic{color:var(--white)}
.frame{left:103px;top:44px;width:562px;height:352px}
.nav{left:94px;top:63px;width:582px;height:30px;background:var(--nav-green);font-family:"Oswald",sans-serif;font-size:8.5px;color:var(--white)}
.nav a{position:absolute;top:9px;color:var(--white);text-decoration:none;white-space:nowrap}
.ribbon{top:71px}
.logo-box{left:338px;top:47px;width:100px;height:88px}
.logo-text{position:absolute;left:0;right:0;top:44px;text-align:center;font-family:"Oswald",sans-serif;font-size:12px;line-height:14px;color:var(--magenta);font-weight:500}
.logo-dot{position:absolute;left:40px;top:16px;width:20px;height:20px;border-radius:50%;background:var(--blue)}
.slogan{left:505px;top:158px;width:120px;text-align:center;font-family:"Oswald",sans-serif;font-weight:500;line-height:1}
.slogan .s1{font-size:28px;color:var(--magenta)}
.slogan .s2{font-size:28px;color:var(--magenta);margin-top:5px}
.slogan .s2 span{font-size:16px;color:var(--lime)}
.slogan .s3{font-size:17px;color:var(--lime);margin-top:3px}
.slogan .s4{font-size:28px;color:var(--blue);margin-top:7px}
.dots{left:548px;top:314px;display:flex;gap:7px}
.dots i{width:6px;height:6px;border-radius:50%;background:#8c8c8c;display:block}
.dots i:first-child{background:var(--magenta)}
.content{left:103px;top:446px;width:562px;height:520px;background:var(--white)}
.welcome{left:0;right:0;top:16px;text-align:center;font-family:"Oswald",sans-serif;font-size:19px;color:var(--ink-dark)}
.welcome b,.col h2 b{font-weight:400;color:var(--blue)}
.divider{left:25px;right:25px;top:52px;height:1px;background:#ddd}
.divider-mark{left:273px;top:45px;width:16px;height:16px;border-radius:50%;background:var(--white);border:2px solid #aaa}
.intro{left:10px;right:10px;top:70px;text-align:center;font-size:7.4px;line-height:12.4px;color:var(--ink)}
.intro a{color:var(--blue)}
.band{left:97px;top:589px;width:575px;height:157px;background:var(--band-blue);border-radius:3px}
.card{top:603px;width:172px;height:129px;background:var(--white)}
.card .photo{height:100px}
.card .label{text-align:center;font-family:"Oswald",sans-serif;font-size:13px;color:var(--pink);padding-top:5px}
.pin{width:14px;height:14px;border-radius:50%;top:596px}
.col{top:765px}
.col h2{font-family:"Oswald",sans-serif;font-weight:400;font-size:13.5px;color:var(--ink-dark);padding-bottom:6px;border-bottom:1px solid #ddd}
.why p{font-size:7.4px;line-height:12.3px;letter-spacing:.3px;margin-top:8px}
.btn{display:block;width:47px;height:16px;background:var(--magenta);color:var(--white);font-size:6.8px;font-weight:700;text-align:center;line-height:16px}
.news-item{display:flex;gap:6px;margin-top:10px}
.news-item:first-of-type{margin-top:9px}
.date{width:24px;height:25px;background:var(--blue);color:var(--white);text-align:center;font-family:"Oswald",sans-serif;font-size:9px;line-height:14px;flex:none}
.date small{display:block;background:var(--magenta);font-family:"Lato",sans-serif;font-size:5px;line-height:8px;font-weight:700}
.news-item h3{font-size:7.5px;font-weight:700;color:var(--blue);line-height:9px}
.news-item p{font-size:7.2px;line-height:9.5px}
.form .field{display:flex;align-items:flex-start;margin-top:6px}
.form label{width:35px;text-align:right;font-size:7.2px;padding-top:5px;margin-right:4px}
.form .box{width:129px;height:17px;border:1px solid #ccc}
.form .box.tall{height:40px}
.footer-art{left:47px;top:962px;width:675px;height:165px;border-radius:6px;background:linear-gradient(180deg,var(--wood-light),var(--wood-dark))}
.grass{left:0;top:1122px;width:768px;height:78px;background:linear-gradient(180deg,#9dd13a,#4f9a1f)}
.foot{color:var(--white);font-size:7.4px;font-weight:700}
.foot h4{font-size:9.5px;font-weight:400;padding-bottom:4px;border-bottom:1px solid #f3c58f}
.links{display:grid;grid-template-columns:96px 80px;row-gap:6px;margin-top:5px;color:var(--bark)}
.contact-list div{display:flex;align-items:center;gap:6px;margin-top:6px;color:var(--bark)}
.contact-list svg{width:8px;height:8px;fill:var(--white);flex:none}
.foot-logo{left:320px;top:1012px;width:128px;text-align:center;font-family:"Oswald",sans-serif;font-size:12px;line-height:14px;font-weight:500;color:#5a3c1c}
.hours{left:300px;top:1048px;width:168px;text-align:center;color:var(--bark);font-size:7.4px;font-weight:700}
.social{left:344px;top:1074px;display:flex;gap:5px}
.social i{width:17px;height:17px;display:block}
.copy{left:0;width:768px;top:1107px;text-align:center;font-size:6px;color:var(--white);font-weight:700}
</style>
</head>
<body>
<div class="scenery" role="img" aria-label="Illustrated landscape of blue sky with clouds, butterflies, rolling green hills and trees"></div>

<div class="abs topbar" style="left:104px;top:5px">
  <div class="row"><svg viewBox="0 0 10 10"><path d="M2 1l2 2-1 1.2c.6 1.2 1.5 2.1 2.8 2.8L7 6l2 2-1.3 1.3C4.5 9 1 5.5.7 2.3z" fill="#fff"/></svg>555-318-7042</div>
  <div class="row"><svg viewBox="0 0 10 10"><rect x="2.5" y="1" width="5" height="3" fill="#fff"/><rect x="1" y="4" width="8" height="4" rx="1" fill="#fff"/><rect x="3" y="6.5" width="4" height="3" fill="#ddd"/></svg>555-318-7049</div>
</div>
<div class="abs topbar right">
  <div>3817 Route 221 N. Harlowville, NJ 08719</div>
  <div class="lic">Fully Licensed for children 6m - 6 years</div>
</div>

<svg class="abs frame" viewBox="0 0 562 352" width="562" height="352">
  <defs>
    <linearGradient id="photoTone" x1="0" y1="0" x2="1" y2="1">
      <stop offset="0" stop-color="#d9b887"/><stop offset=".5" stop-color="#c99476"/><stop offset="1" stop-color="#8a7a6a"/>
    </linearGradient>
  </defs>
  <path d="M0 0H562V310C470 268 400 292 300 320 180 355 80 358 0 346Z" fill="#fff"/>
  <path d="M5 5H557V305C470 264 400 288 300 316 180 350 80 352 5 340Z" fill="#f2f2f2"/>
  <path role="img" aria-label="Photo of a teacher and two toddlers playing with a wooden dollhouse" d="M5 95H380C400 140 410 230 380 300 330 320 250 345 160 348 90 350 40 345 5 340Z" fill="url(#photoTone)"/>
</svg>

<svg class="abs ribbon" style="left:60px" width="44" height="30" viewBox="0 0 44 30"><path d="M0 0H44V30H0L14 15Z" fill="#7ab832"/></svg>
<svg class="abs ribbon" style="left:664px" width="44" height="30" viewBox="0 0 44 30"><path d="M0 0H44L30 15 44 30H0Z" fill="#7ab832"/></svg>

<nav class="abs nav">
  <a style="left:20px">Home</a>
  <a style="left:55px">About</a>
  <a style="left:90px">Programs &amp; Curriculum</a>
  <a style="left:180px">Find Our Center</a>
  <a style="left:360px">Family Resources</a>
  <a style="left:429px">News &amp; Events</a>
  <a style="left:488px">Gallery</a>
  <a style="left:526px">Contact Us</a>
</nav>

<div class="abs logo-box">
  <svg width="100" height="88" viewBox="0 0 100 88" style="position:absolute;left:0;top:0"><path d="M0 0H100V70L50 88 0 70Z" fill="#fff"/></svg>
  <span class="logo-dot"></span>
  <div class="logo-text">MAPLEBROOK<br>ACADEMY</div>
</div>

<div class="abs slogan">
  <div class="s1">WHERE</div>
  <div class="s2">EVERY <span>CHILD</span></div>
  <div class="s3">GETS A TURN TO</div>
  <div class="s4">LEARN</div>
</div>
<div class="abs dots"><i></i><i></i><i></i></div>

<section class="abs content">
  <h1 class="abs welcome" style="font-weight:400">Welcome to <b>Maplebrook Academy</b></h1>
  <div class="abs divider"></div>
  <div class="abs divider-mark"></div>
  <p class="abs intro">Sed ut perspiciatis unde omnis iste natus error sit voluptatem accusantium doloremque laudantium, totam rem aperiam, eaque ipsa quae ab illo inventore veritatis et quasi architecto beatae vitae dicta sunt explicabo. Nemo enim ipsam voluptatem quia voluptas sit aspernatur aut odit aut voluptas sit aspernatur aut odit aut fugit. Sed ut perspiciatis unde omnis iste natus error sit voluptatem accusantium doloremque laudantium, totam rem aperiam, eaque ipsa quae ab illo. Nemo enim ipsam voluptatem quia voluptas sit aspernatur aut odit aut voluptas sit aspernatur aut odit aut fugit.<a href="#">More</a></p>
</section>

<div class="abs band"></div>
<div class="abs card" style="left:113px"><div class="photo" role="img" aria-label="Photo of a teacher and children gathered around a tablet" style="background:linear-gradient(135deg,#c9a27e,#6f8fb8)"></div><div class="label">Programs &amp; Curriculum</div></div>
<div class="abs card" style="left:298px"><div class="photo" role="img" aria-label="Photo of preschoolers doing crafts at a table" style="background:linear-gradient(135deg,#e8d8c8,#d9a0a0)"></div><div class="label">Enrichment Programs</div></div>
<div class="abs card" style="left:484px"><div class="photo" role="img" aria-label="Photo of a coach with children holding a soccer ball on a field" style="background:linear-gradient(135deg,#7a8f3a,#c8b446)"></div><div class="label">Equipment &amp; Facilities</div></div>
<span class="abs pin" style="left:196px;background:#d9232a"></span>
<span class="abs pin" style="left:381px;background:#76c043"></span>
<span class="abs pin" style="left:571px;background:#8a3fb0"></span>

<section class="abs col why" style="left:114px;width:162px">
  <h2>Why <b>Maplebrook Academy?</b></h2>
  <p>Sed ut perspiciatis unde omnis iste natus error sit voluptatem accusantium doloremque laudantium, totam rem aperiam, eaque ipsa quae ab illo inventore veritatis et quasi arc hite cto beatae vitae dicta sunt explicabo. Nemo enim ipsam voluptatem quia voluptas sit aspernatur aut odit aut voluptas sit aspernatur aut odit aut fugit.</p>
</section>
<a class="abs btn" style="left:113px;top:927px">Read More</a>

<section class="abs col" style="left:301px;width:165px">
  <h2>Latest <b>News</b></h2>
  <div class="news-item"><div class="date">10<small>July</small></div><div><h3>Vero eros accumsaet odio</h3><p>Quis nostrud exetiperj suscipit moli ofh lobtis nisl ut aliquip commod.</p></div></div>
  <div class="news-item"><div class="date">10<small>July</small></div><div><h3>Vero eros accumsaet odio</h3><p>Quis nostrud exetiperj suscipit moli ofh lobtis nisl ut aliquip commod.</p></div></div>
  <div class="news-item"><div class="date">10<small>July</small></div><div><h3>Vero eros accumsaet odio</h3><p>Quis nostrud exetiperj suscipit moli ofh lobtis nisl ut aliquip commod.</p></div></div>
</section>
<a class="abs btn" style="left:300px;top:927px">Read More</a>

<section class="abs col form" style="left:489px;width:167px">
  <h2>Quick <b>Inquiry</b></h2>
  <div class="field" style="margin-top:9px"><label>Name:</label><span class="box"></span></div>
  <div class="field"><label>Company:</label><span class="box"></span></div>
  <div class="field"><label>Subject:</label><span class="box"></span></div>
  <div class="field"><label>Message:</label><span class="box tall"></span></div>
</section>
<a class="abs btn" style="left:527px;top:927px">Submit</a>

<div class="abs grass" role="img" aria-label="Illustrated grass along the bottom edge"></div>
<div class="abs footer-art" role="img" aria-label="Illustrated wooden park bench holding the footer"></div>

<div class="abs foot" style="left:118px;top:975px;width:158px">
  <h4>Quick Link</h4>
  <div class="links"><span>Home</span><span>Family Resources</span><span>About</span><span>News &amp; Events</span><span>Programs &amp; Curriculum</span><span>Gallery</span><span>Find Our Center</span><span>Contact Us</span></div>
</div>
<div class="abs foot-logo">MAPLEBROOK<br>ACADEMY</div>
<div class="abs hours">Hours of operation: 6:30 am to 6:30 pm</div>
<div class="abs foot contact-list" style="left:522px;top:975px;width:160px">
  <h4>Contact &nbsp;Info</h4>
  <div><svg viewBox="0 0 8 8"><path d="M4 0a3 3 0 013 3c0 2-3 5-3 5S1 5 1 3a3 3 0 013-3z"/></svg>3817 Route 221 N. Harlowville, NJ 08719</div>
  <div><svg viewBox="0 0 10 10"><path d="M2 1l2 2-1 1.2c.6 1.2 1.5 2.1 2.8 2.8L7 6l2 2-1.3 1.3C4.5 9 1 5.5.7 2.3z"/></svg>555-318-7042</div>
  <div><svg viewBox="0 0 10 10"><rect x="2.5" y="1" width="5" height="3"/><rect x="1" y="4" width="8" height="4" rx="1"/></svg>555-318-7049</div>
  <div style="margin-top:9px"><svg viewBox="0 0 10 8"><rect width="10" height="8"/></svg>main@maplebrookacademytx.com</div>
</div>
<div class="abs social"><i style="background:#3b5998"></i><i style="background:#2aa9e0"></i><i style="background:#d7472f"></i><i style="background:#c4302b"></i></div>
<div class="abs copy">Copyright © 2015 &nbsp;Maplebrook Academy. All Right Reserved</div>
</body>
</html>
```